Kiteloft Namecard

We have a regular but rotating group of Actors and Directors who meet weekly. I'd like to make a nametag (first and last names) for each of the participants which would fit on a regular business card. The first name would be over-sized to enable reading at a distance. The background & border should project fun and warmth. The Kiteloft is meant to be a place to play without judgement or negative vibes.

```html
<!DOCTYPE html>
<html lang="en">
<head>
<meta charset="utf-8">
<title>Kiteloft Namecard</title>
<link href="https://fonts.googleapis.com/css2?family=Archivo+Black&family=Roboto:wght@700&display=swap" rel="stylesheet">
<style>
  :root {
    --sky-deep: #1667c2;
    --sky-light: #3aa7e4;
    --sea: #2cc3d6;
    --sea-light: #3dc9d9;
    --foam: #c9eef0;
    --sand: #f3dcb4;
    --sand-dark: #e9cd9b;
    --perforation: #efd6ab;
    --orange-top: #fbb11f;
    --orange-bottom: #ec5a12;
    --ink: #1b1b1b;
    --white: #ffffff;
    --label-red: #e43a1c;
    --skin: #f4c79c;
    --coral: #ee6a3c;
  }
  * { margin: 0; padding: 0; box-sizing: border-box; }
  html, body { width: 1200px; height: 932px; overflow: hidden; background: var(--sand); }
  .namecard { position: relative; width: 1200px; height: 932px; overflow: hidden; }
  .beach-scene {
    position: absolute; inset: 0;
    background: linear-gradient(180deg,
      var(--sky-deep) 0%, var(--sky-light) 24%,
      var(--sea) 32%, var(--sea-light) 44%, var(--foam) 56%,
      var(--sand) 62%, var(--sand-dark) 100%);
  }
  .first-name {
    position: absolute; left: 42px; top: 268px;
    white-space: nowrap;
    font-family: "Archivo Black", sans-serif; font-weight: 400;
    font-size: 164px; line-height: 1; letter-spacing: -3px;
    background: linear-gradient(180deg, var(--orange-top) 20%, var(--orange-bottom) 85%);
    -webkit-background-clip: text; background-clip: text; color: transparent;
    filter: drop-shadow(6px 6px 0 var(--ink));
  }
  .last-name {
    position: absolute; left: 48px; top: 446px;
    white-space: nowrap;
    font-family: "Archivo Black", sans-serif; font-weight: 400;
    font-size: 80px; line-height: 1; color: var(--white);
    text-shadow: 3px 3px 0 #333, -1px -1px 0 #555;
  }
  .group-name {
    position: absolute; left: 46px; top: 548px;
    font-family: "Roboto", sans-serif; font-weight: 700;
    font-size: 24px; color: var(--label-red);
  }
  .kids-illustration {
    position: absolute; left: 108px; top: 596px; width: 486px; height: 326px;
    border-radius: 24px;
    background: radial-gradient(ellipse at 50% 55%, var(--skin) 0%, rgba(244,199,156,0.6) 50%, rgba(244,199,156,0) 80%);
  }
  .photo-stamp { position: absolute; left: 660px; top: 544px; width: 334px; height: 400px; }
  .crab-illustration {
    position: absolute; left: 1000px; top: 730px; width: 200px; height: 150px;
    border-radius: 16px 0 0 16px;
    background: linear-gradient(180deg, rgba(238,106,60,0.55) 0%, rgba(226,67,29,0.55) 100%);
  }
</style>
</head>
<body>
<main class="namecard">
  <div class="beach-scene" role="img" aria-label="Sunny tropical beach with blue sky, sparkling sea, palm fronds and sand"></div>

  <h1 class="first-name">MARCELLO</h1>
  <h2 class="last-name">ALVARES</h2>
  <p class="group-name">The Kiteloft</p>

  <div class="kids-illustration" role="img" aria-label="Illustration of two children building a sandcastle on the beach"></div>

  <svg class="photo-stamp" viewBox="0 0 334 400" aria-label="Photo frame">
    <defs>
      <linearGradient id="photo-shade" x1="0" y1="0" x2="1" y2="1">
        <stop offset="0" stop-color="#3a3a3a"/>
        <stop offset="0.45" stop-color="#161616"/>
        <stop offset="1" stop-color="#050505"/>
      </linearGradient>
      <pattern id="perforation" width="18" height="18" patternUnits="userSpaceOnUse">
        <circle cx="9" cy="9" r="6" fill="var(--perforation)"/>
      </pattern>
    </defs>
    <rect x="6" y="6" width="322" height="394" fill="var(--white)"/>
    <rect x="6" y="-3" width="322" height="18" fill="url(#perforation)"/>
    <rect x="-3" y="6" width="18" height="394" fill="url(#perforation)"/>
    <rect x="319" y="6" width="18" height="394" fill="url(#perforation)"/>
    <rect x="20" y="24" width="292" height="376" fill="url(#photo-shade)"/>
    <path d="M230 24 C 290 110, 292 260, 250 400 L 312 400 L 312 24 Z" fill="#ffffff" opacity="0.07"/>
  </svg>

  <div class="crab-illustration" role="img" aria-label="Illustration of a red crab claw beside the photo frame"></div>
</main>
</body>
</html>
```